Lantern & Mend Email Marketing

We need an email newsletter design/template that can help us advertise our services and explain what our company is all about. Although we have a lot of text, we'd like something inviting and simple, perhaps with a powerful banner/images and really clear, precise graphics and touches that make the email look inviting and stand out.

Because this will be blasted to many people, we'd like them to take a second look. So the design and layout must really be top notch prior to the reader actually taking time to read the content.

Lantern & Mend is basically a health consultancy that helps patients all over Africa, organize and facilitate their health care in South Africa. So say a person was sick in Kenya. That person might want to go to South Africa, best known for treatment and health care in the continent, however, they might not know where to start looking for doctors, hospitals, or even accommodation and logistics. That is where Lantern & Mend comes in. They take care of all of those things for you, by allowing you to consult with a Doctor who can advise you and arrange all of those logistical nightmares.

******Also the Newsletter we want to put up is uploaded in the Microsoft Word document. Please use the content in the document.******

******And we may look to get someone to code the design as an HTML, so we're looking for really good designs.********

Target Market(s)

The target market is well to do people who would spend money to travel to South Africa for medical treatment. So these people are well travelled, college educated, well to do.

Industry/Entity Type

Accommodation

Font styles to use
Serif

Requirements
Must have
• Include the logo in the header,
Include an area for social media contact details/icons in the footer
Nice to have
• A clean, nice image or graphic health related that makes up the header

```html
<!DOCTYPE html>
<html lang="en">
<head>
<meta charset="utf-8">
<title>Lantern &amp; Mend Newsletter</title>
<link href="https://fonts.googleapis.com/css2?family=Arimo:wght@400;700&display=swap" rel="stylesheet">
<style>
  :root {
    --page-bg: #efefef;
    --top-band: #e2e2e2;
    --sheet: #ffffff;
    --heading-green: #6b9e4c;
    --accent-green: #5db532;
    --body-text: #6a6a6a;
    --strong-text: #3c3c3c;
    --rule: #e3e3e3;
    --social-band: #ebebeb;
    --social-dot: #dcdcdc;
    --footer-bg: #383a4a;
    --footer-text: #ffffff;
    --footer-muted: #a9abb8;
    --square-1: #3b5a9a;
    --square-2: #2aa3dc;
    --square-3: #1d6fa5;
  }
  * { margin: 0; padding: 0; box-sizing: border-box; }
  html, body { width: 1200px; height: 2263px; overflow: hidden; }
  body {
    background: linear-gradient(var(--top-band) 0 121px, var(--page-bg) 121px);
    font-family: "Arimo", Arial, sans-serif;
    color: var(--body-text);
    position: relative;
  }
  .sheet {
    position: absolute; left: 240px; top: 0; width: 720px; height: 1816px;
    background: var(--sheet);
  }
  .inner { position: absolute; left: 36px; width: 648px; }
  .brand {
    position: absolute; left: 27px; top: 36px;
    display: flex; align-items: center; gap: 12px;
    font-size: 40px; font-weight: 700; color: var(--accent-green); letter-spacing: 0.5px;
  }
  .brand-dot { width: 28px; height: 28px; border-radius: 50%; background: var(--accent-green); }
  .header-social { position: absolute; right: 36px; top: 27px; display: flex; gap: 14px; }
  .header-social span { width: 30px; height: 30px; border-radius: 3px; display: block; }
  .header-social span:nth-child(1) { background: var(--square-1); }
  .header-social span:nth-child(2) { background: var(--square-2); }
  .header-social span:nth-child(3) { background: var(--square-3); }
  .call-line { position: absolute; right: 47px; top: 66px; font-size: 18px; color: #8a8a8a; letter-spacing: -0.3px; }
  .call-line b, .green { color: var(--accent-green); font-weight: 700; }
  .hero {
    top: 155px; height: 301px;
    background: linear-gradient(90deg, #e8e4df 0%, #d9d2c8 30%, #b9c79c 60%, #cfd8c2 85%, #5d7f70 100%);
  }
  h1, h2 { color: var(--heading-green); font-weight: 700; }
  .headline { top: 470px; font-size: 22.5px; line-height: 30px; }
  .copy { font-size: 16px; line-height: 24px; }
  .copy strong { color: var(--strong-text); }
  .intro { top: 548px; }
  .intro p + p { margin-top: 24px; }
  .columns { top: 785px; display: flex; justify-content: space-between; }
  .col { width: 307px; }
  .col-photo { height: 143px; }
  .col-photo.doctor { background: linear-gradient(90deg, #dfe6ea, #f3f4f4 45%, #c7d9b4); }
  .col-photo.couple { background: linear-gradient(90deg, #cfd6d8, #d7b9a5 35%, #e3e1dc 65%, #9db7cf); }
  .col h2 { font-size: 21px; margin-top: 18px; margin-bottom: 8px; }
  .center-block { top: 1200px; text-align: center; }
  .contact { margin-top: 24px; }
  .contact a, .footer a { color: var(--accent-green); font-weight: 700; text-decoration: none; border-bottom: 1px solid var(--accent-green); }
  .divider { top: 1373px; height: 1px; background: var(--rule); }
  .services-title { top: 1402px; font-size: 21px; line-height: 30px; }
  .services { top: 1475px; list-style: none; font-size: 16px; line-height: 22px; }
  .services li { margin-bottom: 11px; padding-left: 11px; text-indent: -11px; }
  .services li::before { content: "• "; }
  .social-band {
    position: absolute; left: 240px; top: 1816px; width: 720px; height: 90px;
    background: var(--social-band);
  }
  .social-band h3 { position: absolute; left: 36px; top: 32px; font-size: 21px; font-weight: 400; color: #2f3140; letter-spacing: -0.3px; }
  .social-dots { position: absolute; right: 40px; top: 24px; display: flex; gap: 10px; }
  .social-dots span { width: 41px; height: 41px; border-radius: 50%; background: var(--social-dot); display: block; }
  .footer {
    position: absolute; left: 240px; top: 1906px; width: 720px; height: 234px;
    background: var(--footer-bg); color: var(--footer-text); text-align: center;
    font-size: 16px; line-height: 29px;
  }
  .footer .lead { position: absolute; left: 36px; width: 648px; top: 22px; }
  .footer .lead a { color: var(--footer-text); font-weight: 400; border-bottom-color: var(--footer-text); }
  .footer .reach { position: absolute; left: 0; width: 720px; top: 107px; line-height: 25px; }
  .footer .rule { position: absolute; left: 36px; width: 648px; top: 176px; height: 1px; background: #5a5c6b; }
  .footer .legal { position: absolute; left: 36px; width: 648px; top: 192px; display: flex; justify-content: space-between; font-size: 13.5px; color: var(--footer-muted); }
  .footer .legal b { color: var(--footer-text); font-weight: 400; }
</style>
</head>
<body>
  <main class="sheet">
    <header>
      <div class="brand"><span>Lantern &amp; Mend</span><span class="brand-dot"></span></div>
      <div class="header-social" aria-label="Social links"><span></span><span></span><span></span></div>
      <p class="call-line">Call us today: <b>+1800.555.0142</b></p>
    </header>

    <div class="inner hero" role="img" aria-label="Photo of a doctor with her hand on a smiling patient's shoulder"></div>

    <h1 class="inner headline">Health is a Priority and Not an Option! Don't take chances when options are very close to home!</h1>

    <section class="inner intro copy">
      <p><strong>Lantern &amp; Mend (L&amp;M)</strong> is your link to excellent health care in South Africa. Whether you are suffering from general ill health, require emergency medical attention or need preventative health care, Lantern and Mend can HELP you. It was founded and is managed by Dr. Nala Kimaro, a Tanzanian doctor who knows all too well that misdiagnosis in the African continent is common and health issues are very often mistreated due to a lack of specialized medical knowledge and poor medical facilities.</p>
      <p>This leads to premature death and chronic disability.</p>
    </section>

    <section class="inner columns">
      <article class="col copy">
        <div class="col-photo doctor" role="img" aria-label="Photo of a smiling doctor at his desk"></div>
        <h2>Dr. Nala is a phone call away</h2>
        <p>A doctor trained to manage your chronic/longstanding illness or emergency situation – by providing advice, ensuring that your health condition is accurately diagnosed, and linking you to the <strong>best solution possible as close to home</strong> as possible.</p>
      </article>
      <article class="col copy">
        <div class="col-photo couple" role="img" aria-label="Photo of a smiling senior couple"></div>
        <h2>Best Health Care System</h2>
        <p>There is no doubt that South Africa offers the <strong>best health care system within the African Continent</strong> and Dr. Nala and her team, will manage a medical evacuation from your home country and provide support throughout the treatment process in South Africa.</p>
      </article>
    </section>

    <section class="inner center-block copy">
      <p>By contacting Lantern and Mend, you will have the comfort that you and your family can experience a <strong>seamless and hassle-free</strong> patient journey process.</p>
      <p class="contact">Phone: <span class="green">+1800.555.0142</span><br>Email: <a href="#">info@lanternmend.com</a></p>
    </section>

    <div class="inner divider"></div>

    <h2 class="inner services-title">Lantern&amp; Mend will facilitate the following services for your patient journey process:</h2>
    <ul class="inner services">
      <li>Initial contact with a health care professional to ensure you are guided to an appropriate specialist who can manage your health problem</li>
      <li>Provide access to the most reputable hospitals and healthcare providers in SA</li>
      <li>Schedule appointments with specialists</li>
      <li>Manage all travel arrangements</li>
      <li>Organise hotel or chosen accommodation option</li>
      <li>Transport to and from the airport</li>
      <li>Transport to and from hospital (for all your medical requirements)</li>
      <li>Access to medical evacuation services from home country – Air Ambulance Service</li>
    </ul>
  </main>

  <section class="social-band">
    <h3>STAY CONNECTED</h3>
    <div class="social-dots" aria-label="Social links"><span></span><span></span><span></span><span></span><span></span><span></span><span></span><span></span></div>
  </section>

  <footer class="footer">
    <p class="lead">For further information, visit our website: &nbsp;<a href="#">ww.lanternandmend.co.za</a> or contact us with information provided below.</p>
    <p class="reach">Phone: <span class="green">+1800.555.0142</span><br>Email: <a href="#">info@lanternmend.com</a></p>
    <div class="rule"></div>
    <div class="legal"><span>Copyright 2014 <b>Lantern and Mend</b>. All Rights Reserved.</span><span>View Online &nbsp;|&nbsp; Unsubscribe</span></div>
  </footer>
</body>
</html>
```